New product launches for online boutique

We are looking for an email template, social media template for whenever we launch s new product. We are an online boutique for black women. Imagery should be of black women, use of our logo and a spot to highlight new products and areas for a description of new products.
Template for email marketing
Template for Facebook
Template for Instagram
There could be more than one product being launched
Must be able to sell
Include pricing

Target Market(s)

Black women, women of colour, ages 18-30,

Industry/Entity Type

Skin Care

Requirements
Must have
• Company logo, area for products image, area for products description, must be bright clear

```html
<!DOCTYPE html>
<html lang="en">
<head>
<meta charset="utf-8">
<title>Ayo Beauty – Newsletter</title>
<link href="https://fonts.googleapis.com/css2?family=Montserrat:wght@300;400;500;700&display=swap" rel="stylesheet">
<style>
  :root{
    --backdrop:#e6e6e8;
    --paper:#ffffff;
    --sand:#eddcc2;
    --hero-sand:#ead5b3;
    --ink:#1b1b1b;
    --gold:#c48a34;
    --gold-light:#dba955;
    --gold-dark:#b57a27;
    --icon:#6b6b6b;
  }
  *{margin:0;padding:0;box-sizing:border-box}
  html,body{width:814px;height:1200px;overflow:hidden;background:var(--backdrop)}
  body{font-family:"Montserrat",Arial,sans-serif;color:var(--ink)}
  .email{position:absolute;left:41px;top:0;width:732px;height:1200px;background:var(--paper);overflow:hidden}
  .section{position:absolute;left:0;width:100%}

  .header{top:0;height:168px;display:flex;align-items:center;justify-content:center}
  .brand-name{font-weight:500;font-size:44px;letter-spacing:4px;color:var(--gold);text-transform:uppercase}

  .hero{top:168px;height:316px;background:var(--hero-sand)}
  .hero-photo{position:absolute;right:0;top:0;width:440px;height:316px;
    background:linear-gradient(90deg,var(--hero-sand) 0%,#d8b08a 30%,#6a4030 55%,#8a5a40 75%,#d9b39c 100%)}
  .hero-copy{position:absolute;left:59px;top:32px;width:240px}
  .hero-title{font-weight:300;font-size:34px;line-height:40px;letter-spacing:.5px}
  .hero-title strong{font-weight:700;display:block}
  .hero-text{margin-top:8px;font-size:11.5px;line-height:17.3px;font-weight:400}

  .btn{position:absolute;height:30px;border-radius:3px;display:flex;align-items:center;justify-content:center;
    background:linear-gradient(180deg,var(--gold-light),var(--gold-dark));color:#fff;font-weight:500;font-size:12.5px;letter-spacing:.3px}
  .hero .btn{left:59px;top:244px;width:119px}

  .collection{top:484px;height:302px}
  .product-photo{position:absolute;left:73px;top:25px;width:229px;height:222px;
    background:linear-gradient(180deg,#e9efec,#7fa091 60%,#e9ecea);border-radius:4px}
  .collection-copy{position:absolute;left:392px;top:50px;width:280px}
  .collection-title{font-weight:300;font-size:24px;letter-spacing:.3px}
  .collection-text{margin-top:10px;font-size:11px;line-height:17.2px}
  .collection .btn{left:392px;top:213px;width:119px}

  .club{top:786px;height:331px;background:var(--sand);text-align:center}
  .club-title{position:absolute;top:44px;width:100%;font-weight:300;font-size:24px;letter-spacing:.3px}
  .club-text{position:absolute;left:64px;right:64px;top:112px;font-size:11px;line-height:17.2px}
  .club-note{position:absolute;top:206px;width:100%;font-size:11px}
  .club .btn{left:234px;top:238px;width:263px}

  .footer{top:1117px;height:83px}
  .copyright{position:absolute;left:59px;top:22px;font-size:11px}
  .social{position:absolute;right:59px;top:22px;display:flex;gap:15px}
  .social span{display:block;width:19px;height:19px;border-radius:3px;background:var(--icon)}
</style>
</head>
<body>
<div class="email">
  <header class="section header">
    <div class="brand-name">Ayo Beauty</div>
  </header>

  <section class="section hero">
    <div class="hero-photo" role="img" aria-label="Portrait photo of a woman with curly hair in warm golden light"></div>
    <div class="hero-copy">
      <h1 class="hero-title">CATCH THE<br>HOTTEST<strong>DEALS</strong></h1>
      <p class="hero-text">Lorem ipsum dolor sit amet, consectetuer adipiscing elit, sed diam nonummy nibh euismod tincidunt ut laoreet dolore magna aliquam erat volutpat.</p>
    </div>
    <a class="btn">Shop Now</a>
  </section>

  <section class="section collection">
    <div class="product-photo" role="img" aria-label="Product photo of a green cleanser tube, serum bottle and boxed spot treatment"></div>
    <div class="collection-copy">
      <h2 class="collection-title">Best beauty collection</h2>
      <p class="collection-text">Lorem ipsum dolor sit amet, consectetuer adipiscing elit, sed diam nonummy nibh euismod tincidunt ut laoreet dolore magna aliquam erat volutpat. Ut wisi enim ad minim veniam, quis nostrud exerci tation ullamcorper suscipit lobortis nisl ut aliquip ex ea commodo.</p>
    </div>
    <a class="btn">View Products</a>
  </section>

  <section class="section club">
    <h2 class="club-title">Becoming a AYOBEAUTY Enthusiast</h2>
    <p class="club-text">As a Member Of AYOBEAUTY ENTHUSIAST Community, You'll Experience<br>The latest promotions, product rewards and entitles you to a birthday gift during your birthday month.Regular communications and special offers only available to AYOBEAUTY enthusiast's.News of upcoming loyalty incentives or events .</p>
    <p class="club-note">Becoming a AYOBEAUTY Enthusiast is simple and completely free</p>
    <a class="btn">Becoming a AYOBEAUTY Enthusiast</a>
  </section>

  <footer class="section footer">
    <p class="copyright">© 2018 - All Rights Reserved</p>
    <div class="social" aria-label="Social links"><span></span><span></span><span></span></div>
  </footer>
</div>
</body>
</html>
```